Helping Seniors and their families start the discussion about driver safety, and explore options to preserve senior independence.
Target Market(s)
Seniors and their families
Industry/Entity Type
Non Profit
Number of Pages Required
4 page
Font styles to use
Sans Serif
Requirements
Must have
- Logo
- Application for Bright Pathways Registration

Nice to have
- Colorful, and designed for Senior Citizens and their Families

```html
<!DOCTYPE html>
<html lang="en">
<head>
<meta charset="utf-8">
<title>Bright Pathways – A Transportation Networking Company</title>
<link href="https://fonts.googleapis.com/css2?family=Lato:ital,wght@0,400;0,700;0,900;1,400&family=Montserrat:wght@600;700;800&display=swap" rel="stylesheet">
<style>
:root{
  --green:#009a57;
  --green-dark:#007f47;
  --ink:#1e1e1e;
  --text:#333;
  --muted:#777;
  --line:#d9d9d9;
  --gray-bg:#f1f1f1;
  --footer:#232323;
  --footer-bottom:#141414;
  --white:#fff;
}
*{margin:0;padding:0;box-sizing:border-box}
html,body{width:1200px;height:3232px;overflow:hidden;background:var(--white)}
body{font-family:'Lato',sans-serif;color:var(--text);position:relative}
.abs{position:absolute}
.heading{font-family:'Montserrat',sans-serif;font-weight:800;color:var(--ink);font-size:28px;letter-spacing:.5px}
.heading span{color:var(--green)}
.divider{position:absolute;height:1px;background:var(--line)}
.divider::after{content:"";position:absolute;left:50%;top:-8px;width:16px;height:16px;margin-left:-8px;border:1px solid #ccc;border-radius:50%;background:var(--white)}
.btn{position:absolute;display:flex;align-items:center;justify-content:center;background:var(--green);color:var(--white);font-weight:700;font-size:13px;letter-spacing:.3px}
.btn-dark{background:var(--ink)}
.photo{position:absolute}

/* top bar */
.topbar{left:0;top:0;width:1200px;height:32px;background:var(--green);color:var(--white);font-size:13px}
.topbar .item{position:absolute;top:0;height:32px;display:flex;align-items:center;gap:8px}

/* header */
.logo{left:99px;top:44px;display:flex;align-items:center;gap:10px}
.logo .mark{width:30px;height:30px;border-radius:50%;background:var(--green);flex:none}
.logo .name{font-family:'Lato',sans-serif;font-weight:900;font-size:36px;color:var(--green);line-height:35px}
.nav a{position:absolute;top:78px;font-size:13px;color:var(--ink);text-decoration:none;font-weight:400}
.nav a.active{color:var(--green);font-weight:700}
.nav .sep{position:absolute;top:72px;width:1px;height:28px;background:var(--line)}

/* hero */
.hero{left:0;top:134px;width:1200px;height:549px;background:linear-gradient(100deg,#d9c7b4 0%,#c9a58c 20%,#b84a45 38%,#c4262d 55%,#8f2a26 75%,#5b6a3a 100%)}
.hero-tag{position:absolute;display:flex;align-items:center;justify-content:center;font-weight:700;color:var(--white)}

/* services */
.service-card .photo{width:319px;height:172px}
.service-card h3{position:absolute;font-family:'Lato',sans-serif;font-weight:700;font-size:15px;color:var(--ink);letter-spacing:.3px}
.service-card p{position:absolute;font-size:12.5px;line-height:19px;color:#444;width:319px}
.arrow-box{position:absolute;top:776px;width:30px;height:30px;display:flex;align-items:center;justify-content:center}

.reg-panel{left:797px;top:737px;width:304px;height:485px;background:#f6f6f6;box-shadow:0 6px 14px rgba(0,0,0,.18)}
.reg-panel .head{height:56px;background:var(--green);color:var(--white);font-weight:700;font-size:18px;display:flex;align-items:center;justify-content:center;letter-spacing:.3px}
.reg-panel .field{position:absolute;left:22px;width:261px;background:var(--white);border:1px solid #ddd;font-size:12px;font-style:italic;color:#999;padding:8px 10px}

/* why */
.why{left:0;top:1271px;width:1200px;height:384px;background:var(--gray-bg);border-top:1px solid #e2e2e2;border-bottom:1px solid #e2e2e2}
.why p{position:absolute;left:150px;width:900px;text-align:center;font-size:12.5px;line-height:19px;color:#333}

/* participation */
.req{position:absolute;left:407px;width:690px;font-size:16px;line-height:23px;color:var(--ink)}
.req-icon{position:absolute;left:388px}

/* band */
.band{left:0;top:2252px;width:1200px;height:155px;background:var(--green)}

/* testimonials */
.avatar{position:absolute;top:2549px;width:117px;height:117px;border-radius:50%;border:5px solid var(--ink);background:linear-gradient(160deg,#d8d3cc,#8c857c)}
.avatar.active{border-color:var(--green);box-shadow:0 0 0 4px var(--white),0 0 0 6px var(--green)}
.avatar-name{position:absolute;top:2680px;width:200px;text-align:center;font-size:14px;color:var(--ink)}
.quote-box{left:99px;top:2730px;width:1002px;height:140px;border:1px solid var(--line);background:var(--white)}
.quote-box p{position:absolute;left:80px;top:28px;width:842px;text-align:center;font-style:italic;font-size:12.5px;line-height:22px;color:#444}

/* footer */
.footer{left:0;top:2924px;width:1200px;height:261px;background:var(--footer);color:#ddd}
.footer h4{position:absolute;top:40px;font-family:'Lato',sans-serif;font-weight:700;font-size:15px;color:var(--white);letter-spacing:.3px}
.footer .rule{position:absolute;top:66px;height:1px;background:#555}
.footer li{position:absolute;list-style:none;font-size:12.5px;color:#ddd;display:flex;align-items:center;gap:9px}
.social{position:absolute;top:163px;width:24px;height:24px;border-radius:50%;background:var(--white)}
.copy{left:0;top:3185px;width:1200px;height:47px;background:var(--footer-bottom);color:#ccc;font-size:12px;display:flex;align-items:center;justify-content:center}
</style>
</head>
<body>

<!-- top bar -->
<div class="abs topbar">
  <div class="item" style="left:700px">
    <svg width="16" height="12" viewBox="0 0 16 12"><rect x="0" y="0" width="16" height="12" rx="1" fill="#fff"/><path d="M1 1 L8 7 L15 1" stroke="#009a57" stroke-width="1.5" fill="none"/></svg>
    hello@brightpathways.org
  </div>
  <div class="item" style="left:898px">
    <svg width="16" height="16" viewBox="0 0 24 24"><path d="M6.6 10.8a15.1 15.1 0 0 0 6.6 6.6l2.2-2.2c.3-.3.7-.4 1-.2 1.1.4 2.3.6 3.6.6.6 0 1 .4 1 1V20c0 .6-.4 1-1 1C10.6 21 3 13.4 3 4c0-.6.4-1 1-1h3.5c.6 0 1 .4 1 1 0 1.3.2 2.5.6 3.6.1.3 0 .7-.2 1z" fill="#fff"/></svg>
    Need Support? 555 - 014 - 2290
  </div>
</div>

<!-- header -->
<div class="abs logo">
  <div class="mark"></div>
  <div class="name">Bright<br>Pathways</div>
</div>
<nav class="nav">
  <a class="active" href="#" style="left:438px">HOME</a>
  <svg class="abs" style="left:447px;top:100px" width="20" height="20" viewBox="0 0 20 20"><circle cx="10" cy="10" r="8" fill="none" stroke="#ccc"/></svg>
  <span class="sep" style="left:509px"></span>
  <a href="#" style="left:541px">ABOUT US</a>
  <span class="sep" style="left:632px"></span>
  <a href="#" style="left:663px">OUR SERVICE</a>
  <span class="sep" style="left:770px"></span>
  <a href="#" style="left:802px">CONTACT US</a>
  <div class="btn btn-dark" style="left:931px;top:65px;width:170px;height:43px;font-size:13px">MAKE A REGISTRATION</div>
</nav>

<!-- hero -->
<div class="abs hero" role="img" aria-label="Photo of a young woman helping a smiling senior man out of a red car"></div>
<div class="hero-tag" style="left:834px;top:457px;width:267px;height:56px;background:var(--green);font-size:21px;letter-spacing:.5px">BRIGHT PATHWAYS</div>
<div class="hero-tag" style="left:696px;top:521px;width:405px;height:56px;background:var(--ink);font-size:19px">A Transportation Networking Company</div>

<!-- services -->
<h2 class="abs heading" style="left:99px;top:730px">OUR <span>SERVICES</span></h2>
<div class="divider" style="left:99px;top:791px;width:590px"></div>
<div class="arrow-box" style="left:700px;background:#e3e3e3"><svg width="10" height="12" viewBox="0 0 10 12"><path d="M7 1 L2 6 L7 11" stroke="#555" stroke-width="2" fill="none"/></svg></div>
<div class="arrow-box" style="left:733px;background:var(--green)"><svg width="10" height="12" viewBox="0 0 10 12"><path d="M3 1 L8 6 L3 11" stroke="#fff" stroke-width="2" fill="none"/></svg></div>
<div class="abs" style="left:99px;top:821px;font-size:14px;color:var(--ink)">GO WHEN AND WHERE YOU WANT TO GO WITH BRIGHT PATHWAYS!</div>

<div class="service-card">
  <div class="photo" style="left:99px;top:858px;background:linear-gradient(120deg,#e9eef2,#c7d3dc 60%,#9fb0bf)" role="img" aria-label="Photo of a doctor talking with a senior patient"></div>
  <h3 style="left:99px;top:1057px">MEDICAL APPOINTMENT</h3>
  <p style="left:99px;top:1084px">Lorem ipsum dolor sit amet, consectetuer adipiscing el it, sed diam nonummy nibh euismod tincidunt ut laoreet dolore magna aliquam erat volutpat.</p>
  <div class="btn" style="left:99px;top:1166px;width:116px;height:36px;font-size:12px">READ MORE</div>

  <div class="photo" style="left:446px;top:858px;background:linear-gradient(120deg,#f0f0ee,#d5d8d6 55%,#9fa9b0)" role="img" aria-label="Photo of a therapist helping a senior man during physical therapy"></div>
  <h3 style="left:446px;top:1057px">PHYSICAL THERAPY</h3>
  <p style="left:446px;top:1084px">Lorem ipsum dolor sit amet, consectetuer adipiscing el it, sed diam nonummy nibh euismod tincidunt ut laoreet dolore magna aliquam erat volutpat.</p>
  <div class="btn" style="left:446px;top:1166px;width:116px;height:36px;font-size:12px">READ MORE</div>
</div>

<div class="abs reg-panel">
  <div class="head">MAKE A REGISTRATION</div>
  <div class="abs" style="left:22px;top:76px;font-size:18px;color:var(--ink)">Leave a Message</div>
  <div class="abs" style="left:22px;top:109px;width:80px;height:1px;background:#aaa"></div>
  <div class="abs" style="left:22px;top:116px;width:250px;font-size:12px;line-height:17px;color:var(--muted)">Lorem ipsum dolor sit amet, consectetuer adipiscing elit.</div>
  <div class="field" style="top:172px;height:41px">Chapter I.D</div>
  <div class="field" style="top:222px;height:39px">Rider's Name</div>
  <div class="field" style="top:267px;height:76px">Rider's Address</div>
  <div class="field" style="top:353px;height:39px">City &amp; State
    <svg class="abs" style="right:10px;top:15px" width="10" height="6" viewBox="0 0 10 6"><path d="M1 1 L5 5 L9 1" stroke="#999" stroke-width="1.5" fill="none"/></svg>
  </div>
  <div class="btn" style="left:22px;top:407px;width:261px;height:37px;font-size:14px">NEXT STEP</div>
</div>

<!-- why -->
<section class="abs why">
  <h2 class="abs heading" style="left:0;width:1200px;text-align:center;top:42px">WHY <span>BRIGHT PATHWAYS?</span></h2>
  <div class="divider" style="left:99px;top:104px;width:1002px"></div>
  <p style="top:132px">Convenience With Bright Pathways, you can schedule transportation at a time that is convenient for you, eliminating the need to work around the schedule of family and friends. Transportation is not limited to medical appointments. You can travel to the mall, concerts, church, grocery store, theater, etc. Go when and where you want to go!</p>
  <p style="top:204px">Specialized Services Our team is experienced in providing services to seniors and individuals with physical and cognitive issues such as blindness, cancer, hip/knee replacement, Autism, Alzheimer's, loss of hearing, OCD, etc. Safety Your safety is our first priority. We follow you from location to location, and then follow up with you to see how the ride was and if you have questions or concerns.</p>
  <div class="btn" style="left:542px;top:296px;width:116px;height:36px;font-size:12px">READ MORE</div>
</section>

<!-- participation -->
<h2 class="abs heading" style="left:0;width:1200px;text-align:center;top:1698px">PARTICIPATION <span>REQUIREMENTS</span></h2>
<div class="divider" style="left:99px;top:1763px;width:1002px"></div>
<div class="photo" style="left:99px;top:1795px;width:263px;height:403px;border:3px solid var(--green);background:linear-gradient(150deg,#cfd4d6,#9aa2a6 50%,#6f6b68)" role="img" aria-label="Photo of a caregiver helping a senior woman into a car"></div>
<div class="abs" style="left:384px;top:1795px;width:1px;height:403px;background:var(--line)"></div>

<svg class="req-icon" style="top:1841px" width="10" height="16" viewBox="0 0 10 16"><path d="M1 1 L9 8 L1 15Z" fill="#009a57"/></svg>
<div class="req" style="top:1838px">There is a one time registra- tion fee of $10.00 per participant.</div>
<svg class="req-icon" style="top:1916px" width="10" height="16" viewBox="0 0 10 16"><path d="M1 1 L9 8 L1 15Z" fill="#009a57"/></svg>
<div class="req" style="top:1913px">A credit card is required for billing of individual rides.</div>
<svg class="req-icon" style="top:1979px" width="10" height="16" viewBox="0 0 10 16"><path d="M1 1 L9 8 L1 15Z" fill="#009a57"/></svg>
<div class="req" style="top:1976px">We accommodate individuals with mobility needs (folding wheelchairs, walkers and &nbsp;service animals)</div>
<svg class="req-icon" style="top:2063px" width="10" height="16" viewBox="0 0 10 16"><path d="M1 1 L9 8 L1 15Z" fill="#009a57"/></svg>
<div class="req" style="top:2060px">Drivers will not provide per-sonal assistance (no entering home or escorting to appointments)</div>
<svg class="req-icon" style="top:2123px" width="10" height="16" viewBox="0 0 10 16"><path d="M1 1 L9 8 L1 15Z" fill="#009a57"/></svg>
<div class="req" style="top:2120px">Participants must have a cell phone (we have a companion program that offers need based cell phones at little to no cost to seniors meeting &nbsp;qualification requirements.)</div>

<!-- reservation band -->
<div class="abs band">
  <div class="abs" style="left:125px;top:56px;font-family:'Montserrat',sans-serif;font-weight:700;font-size:34px;color:var(--white);letter-spacing:.5px">RESERVATION LINE : 555 - 013 - 7740</div>
  <div class="btn btn-dark" style="left:795px;top:54px;width:276px;height:49px;font-size:15px">VIEW RESERVATION PROCESS</div>
</div>

<!-- testimonials -->
<h2 class="abs heading" style="left:0;width:1200px;text-align:center;top:2451px">CLIENT <span>TESTIMONIALS</span></h2>
<div class="divider" style="left:99px;top:2510px;width:1002px"></div>
<svg class="abs" style="left:184px;top:2593px" width="12" height="24" viewBox="0 0 12 24"><path d="M10 2 L2 12 L10 22" stroke="#ddd" stroke-width="2" fill="none"/></svg>
<svg class="abs" style="left:1000px;top:2593px" width="12" height="24" viewBox="0 0 12 24"><path d="M2 2 L10 12 L2 22" stroke="#ddd" stroke-width="2" fill="none"/></svg>

<div class="avatar active" style="left:233px" role="img" aria-label="Client portrait"></div>
<div class="avatar" style="left:446px" role="img" aria-label="Client portrait"></div>
<div class="avatar" style="left:640px" role="img" aria-label="Client portrait"></div>
<div class="avatar" style="left:843px" role="img" aria-label="Client portrait"></div>
<div class="avatar-name" style="left:191px;color:var(--green)">Lorem Ipsum Dolor</div>
<div class="avatar-name" style="left:404px">Lorem Ipsum Dolor</div>
<div class="avatar-name" style="left:598px">Lorem Ipsum Dolor</div>
<div class="avatar-name" style="left:801px">Lorem Ipsum Dolor</div>

<div class="abs quote-box">
  <svg class="abs" style="left:180px;top:-12px" width="24" height="13" viewBox="0 0 24 13"><path d="M0 12.5 L12 1 L24 12.5" fill="#fff" stroke="#d9d9d9"/></svg>
  <svg class="abs" style="left:40px;top:24px" width="32" height="24" viewBox="0 0 32 24"><path d="M2 22 Q2 6 12 2 L13 5 Q7 9 8 14 L13 14 L13 22Z M18 22 Q18 6 28 2 L29 5 Q23 9 24 14 L29 14 L29 22Z" fill="#d7ece1"/></svg>
  <p>Lorem Ipsum is simply dummy text of the printing and typesetting industry. Lorem Ipsum has been the industry's standard dummy text ever since the 1500s, when an unknown printer took a galley of type and scrambled it to make a type specimen book. It has survived not only five centuries, but also the leap into electronic typesetting, remaining essentially unchanged. It was pn tof Typeworks sheets.</p>
  <svg class="abs" style="left:758px;top:96px" width="32" height="24" viewBox="0 0 32 24"><path d="M30 2 Q30 18 20 22 L19 19 Q25 15 24 10 L19 10 L19 2Z M14 2 Q14 18 4 22 L3 19 Q9 15 8 10 L3 10 L3 2Z" fill="#d7ece1"/></svg>
</div>

<!-- footer -->
<footer class="abs footer">
  <h4 style="left:99px">QUICK LINKS</h4>
  <div class="rule" style="left:99px;width:180px"></div>
  <ul>
    <li style="left:99px;top:84px">›&nbsp; Home</li>
    <li style="left:99px;top:113px">›&nbsp; About Us</li>
    <li style="left:99px;top:141px">›&nbsp; Services</li>
    <li style="left:99px;top:170px">›&nbsp; Contact Us</li>
    <li style="left:99px;top:198px">›&nbsp; Make a Registration</li>
  </ul>

  <h4 style="left:302px">CONTACT DETAIL</h4>
  <div class="rule" style="left:302px;width:250px"></div>
  <ul>
    <li style="left:302px;top:84px;align-items:flex-start">
      <svg width="11" height="15" viewBox="0 0 12 16" style="margin-top:2px"><path d="M6 0C2.7 0 0 2.6 0 5.9 0 10.3 6 16 6 16s6-5.7 6-10.1C12 2.6 9.3 0 6 0zm0 8.2A2.3 2.3 0 1 1 6 3.6a2.3 2.3 0 0 1 0 4.6z" fill="#fff"/></svg>
      <span style="line-height:20px">412 Meadow Lane Suite 210<br>- Fairview, GA 30000</span>
    </li>
    <li style="left:302px;top:141px">
      <svg width="13" height="13" viewBox="0 0 24 24"><path d="M6.6 10.8a15.1 15.1 0 0 0 6.6 6.6l2.2-2.2c.3-.3.7-.4 1-.2 1.1.4 2.3.6 3.6.6.6 0 1 .4 1 1V20c0 .6-.4 1-1 1C10.6 21 3 13.4 3 4c0-.6.4-1 1-1h3.5c.6 0 1 .4 1 1 0 1.3.2 2.5.6 3.6.1.3 0 .7-.2 1z" fill="#fff"/></svg>
      555 - 014 - 2290 (business office)
    </li>
    <li style="left:302px;top:170px">
      <svg width="13" height="13" viewBox="0 0 24 24"><path d="M6.6 10.8a15.1 15.1 0 0 0 6.6 6.6l2.2-2.2c.3-.3.7-.4 1-.2 1.1.4 2.3.6 3.6.6.6 0 1 .4 1 1V20c0 .6-.4 1-1 1C10.6 21 3 13.4 3 4c0-.6.4-1 1-1h3.5c.6 0 1 .4 1 1 0 1.3.2 2.5.6 3.6.1.3 0 .7-.2 1z" fill="#fff"/></svg>
      555 - 013 - 7740
    </li>
    <li style="left:302px;top:198px">
      <svg width="13" height="10" viewBox="0 0 16 12"><rect width="16" height="12" rx="1" fill="#fff"/><path d="M1 1 L8 7 L15 1" stroke="#232323" stroke-width="1.5" fill="none"/></svg>
      hello@brightpathways.org
    </li>
  </ul>

  <h4 style="left:586px">VIEW LOCATION</h4>
  <div class="rule" style="left:586px;width:210px"></div>
  <div class="abs" style="left:586px;top:86px;width:207px;height:100px;background:linear-gradient(135deg,#cfe0ee,#e8eadf 45%,#9dc0dd)" role="img" aria-label="Map showing the office location"></div>

  <div class="abs" style="left:896px;top:89px;width:205px;height:52px;background:var(--white)" role="img" aria-label="Partner badge"></div>
  <div class="social" style="left:917px"></div>
  <div class="social" style="left:945px"></div>
  <div class="social" style="left:973px"></div>
  <div class="social" style="left:1001px"></div>
  <div class="social" style="left:1029px"></div>
  <div class="social" style="left:1057px"></div>
</footer>
<div class="abs copy">copyright © 2017 Bright Pathways. All Rights Reserved</div>

</body>
</html>
```